New Design for our Velorin Gran Reserva Brandy, it is the label design for the bottle label

We need a new bottle label for our Brandy Gran Reserva that we want to bring to the market.

Please have a look at all our current bottles and labels and the feel of our company under www.velorin-example.ch

The bottle that we will be using for the brand is a different one than the one that we already have, the design of the bottle is attached with a document.

I have also attached a briefing in regards to Brandy in general for your information.

### 1. What is Brandy?
Brandy is a distilled spirit made from fermented wine or other fruit wines. It is traditionally aged in oak barrels, which gives it its characteristic color and rich flavor. The aging process in oak is essential for developing the aromas and quality of the brandy.

### 2. What is Brandy Reserva?
A Brandy labeled as "Reserva" has undergone a longer aging process, typically at least 2 to 3 years, in oak barrels. This aging gives the brandy a deeper, more complex flavor profile and a darker color. "Reserva" is often an indication of higher quality.

### 3. Who enjoys drinking Brandy?
Brandy is typically favored by those who appreciate a deep, rich tasting experience. This often includes older consumers who value the time-aged complexity of the spirit. However, Brandy is also gaining popularity among younger people, especially through cocktails and modern serving styles.

### 4. Why is Brandy trending?
Brandy is experiencing a resurgence as consumers increasingly value quality and artisanal production methods. Its versatility in cocktails and association with traditional, luxurious experiences have also contributed to its renewed popularity.

### 5. What colors would be associated with Brandy?
The typical colors associated with Brandy are warm gold, amber, and deep golden-brown tones. These colors reflect the aging process in oak barrels and the richness of the flavors. Other associated colors might include dark brown and mahogany.

### 6. What is important to customers when buying Brandy?
Customers care about the origin of the Brandy, the aging time, the quality of the ingredients, the production method, and the brand. They also pay attention to the prestige of the product and the authenticity of the production.

### 7. What is not important to customers when buying Brandy?
For many customers, the price and packaging (unless it’s especially exclusive) may be less important than the quality and taste of the Brandy. The distillery name might be less significant if it isn’t tied to a particular reputation.

### 8. What do customers know about Swiss Brandy?
Swiss Brandy is still relatively unknown in many markets, but customers who are familiar with it appreciate the precision and quality of Swiss production. Swiss Brandy is assumed to be made with care and under strict quality standards.

### 9. What is Brandy Gran Reserva?
**Brandy Gran Reserva** is an even higher quality and longer-aged version of Brandy. Generally, a Gran Reserva is aged for at least 5 to 10 years or more in oak barrels. This extended aging process gives the Brandy an especially deep, complex flavor profile and often a darker, richer color. Gran Reserva is often regarded as the top-tier product within a Brandy range and appeals to discerning consumers who value quality, refinement, and a luxurious tasting experience.

The label “Gran Reserva” thus indicates the highest quality level for Brandies, similar to other spirits (like wine or whisky), where the aging time is a critical factor.

### 10. What emotions are associated with Brandy?
Brandy is often associated with luxury, relaxation, and comfort. It evokes feelings of tradition, elegance, and sophistication. Drinking Brandy is frequently seen as a moment of reflection and enjoyment.

### 11. How should Brandy be marketed?
Brandy should be marketed with a focus on its artisanal production, quality, and tradition. A narrative around the product, its aging, and origin can help create an emotional connection with the customer. The marketing should also emphasize the versatility of Brandy, whether consumed neat or in cocktails.

### 12. Sales test and label design for Velorin Brandy
For a sales test, I would suggest a tasting in an upscale setting, perhaps paired with a storytelling presentation highlighting the history of the 6-year aged Brandy and its aging in oak barrels.

**Label design**:
The label should reflect the exclusivity of the product, with an elegant, minimalist design. Colors like deep gold, mahogany, and a hint of deep blue could be used to emphasize the aging and quality of the Brandy. The label should include information about the aging time, the use of oak barrels, and a brief story about the Brandy’s production. A seal or embossing highlighting the craftsmanship would also be fitting.

Target Market(s)

Customers that like Brandy

Requirements
Must have
• the Alcohol % must be included on the label as well as our address.

```html
<!DOCTYPE html>
<html lang="en">
<head>
<meta charset="utf-8">
<title>Velorin Gran Reserva Brandy – Label</title>
<link rel="stylesheet" href="https://fonts.googleapis.com/css2?family=Cinzel:wght@400;600;700&family=Cormorant+Garamond:ital,wght@1,400;1,600&family=Mrs+Saint+Delafield&display=swap">
<style>
  :root{
    --bg:#ffffff;
    --navy:#163a5c;
    --navy-deep:#0d2a45;
    --night:#08121f;
    --gold:#b8913e;
    --gold-light:#d4b46a;
    --cream:#f2ede2;
    --ink:#4a4a4a;
    --ink-soft:#7a766e;
    --silver:#e9eaec;
    --seal:#a3121a;
    --neck-black:#14110e;
    --swiss-red:#d52b1e;
  }
  *{margin:0;padding:0;box-sizing:border-box}
  html,body{width:1200px;height:1200px;overflow:hidden;background:var(--bg)}
  .canvas{position:relative;width:1200px;height:1200px}

  /* Neck label */
  .neck-label{position:absolute;left:190px;top:232px;width:112px;height:462px;border-radius:6px;overflow:hidden;background:var(--cream);box-shadow:0 0 0 1px #e4e0d6}
  .neck-label__band{position:absolute;left:0;top:0;width:112px;height:330px;background:var(--neck-black)}
  .neck-label__edge{position:absolute;left:0;top:330px}
  .neck-label__title{position:absolute;left:56px;top:165px;transform:translate(-50%,-50%) rotate(-90deg);white-space:nowrap;font-family:'Cinzel',serif;font-weight:700;font-size:27px;letter-spacing:2px;color:var(--gold)}
  .neck-label__sub{position:absolute;left:0;width:112px;top:358px;text-align:center;font-family:'Cinzel',serif;font-weight:600;font-size:10px;line-height:10px;color:var(--gold)}
  .neck-label__script{position:absolute;left:0;width:104px;top:384px;text-align:center;font-family:'Mrs Saint Delafield',cursive;font-size:34px;line-height:1;color:#2d2d2d}

  /* Front label */
  .front-label{position:absolute;left:400px;top:232px;width:650px;height:735px;border-radius:10px;overflow:hidden;background:var(--navy)}
  .front-label__mountains{position:absolute;left:0;top:150px;width:650px;height:432px;background:linear-gradient(180deg,rgba(22,58,92,0) 0%,#2a5478 45%,#1c4268 75%,#183c5f 100%)}
  .front-label__base{position:absolute;left:0;top:582px;width:650px;height:153px;background:var(--night)}
  .swiss-flag{position:absolute;left:309px;top:38px;width:32px;height:20px;background:var(--swiss-red)}
  .swiss-flag::before,.swiss-flag::after{content:"";position:absolute;background:#fff}
  .swiss-flag::before{left:14px;top:4px;width:4px;height:12px}
  .swiss-flag::after{left:10px;top:8px;width:12px;height:4px}
  .brand-name{position:absolute;left:0;width:650px;top:64px;text-align:center;font-family:'Cinzel',serif;font-weight:700;font-size:52px;letter-spacing:3px;color:var(--gold)}
  .brand-tagline{position:absolute;left:0;width:650px;top:136px;text-align:center;font-family:'Cinzel',serif;font-weight:600;font-size:12px;letter-spacing:1.5px;color:#e6e6e6}
  .product-title{position:absolute;left:0;width:650px;top:292px;text-align:center;font-family:'Cinzel',serif;font-weight:700;font-size:50px;letter-spacing:3px;color:var(--gold)}
  .product-subtitle{position:absolute;left:0;width:650px;top:350px;text-align:center;font-family:'Cinzel',serif;font-weight:600;font-size:19px;letter-spacing:1.5px;color:var(--gold)}
  .product-type{position:absolute;left:0;width:650px;top:396px;text-align:center;font-family:'Mrs Saint Delafield',cursive;font-size:86px;line-height:1;color:var(--silver)}

  .info-panel{position:absolute;left:88px;top:497px;width:496px;height:180px}
  .info-panel svg{position:absolute;left:0;top:0}
  .info-panel__story{position:absolute;left:30px;top:22px;width:182px;font-family:'Cormorant Garamond',serif;font-style:italic;font-size:10.5px;line-height:17px;color:var(--ink-soft)}
  .info-panel__age{position:absolute;left:212px;top:18px;width:76px;text-align:center;font-family:'Cinzel',serif;color:var(--ink)}
  .info-panel__age-label{font-size:15px;color:var(--gold);font-weight:600}
  .info-panel__age-number{font-size:52px;line-height:44px;font-weight:700;color:#3a3a3a}
  .info-panel__age-unit{font-size:15px;color:var(--gold);font-weight:600}
  .tasting-notes{position:absolute;left:296px;top:22px;width:190px;list-style:none;font-family:'Cormorant Garamond',serif;font-style:italic;font-size:10.5px;line-height:17px;color:var(--ink-soft)}
  .tasting-notes b{color:#3a3a3a;font-weight:600}
  .info-panel__barrels{position:absolute;left:0;width:496px;top:108px;display:flex;justify-content:center;align-items:center;gap:8px;font-family:'Cinzel',serif;font-size:13px;letter-spacing:1px;color:var(--ink-soft)}
  .barrel-icon{width:36px;height:30px;border-radius:6px;background:linear-gradient(180deg,#c9c6bf,#8d8a84)}
  .info-panel__abv{position:absolute;left:0;width:496px;top:140px;text-align:center;font-family:'Cinzel',serif;font-weight:600;font-size:11px;letter-spacing:1px;color:var(--gold)}
  .craft-seal{position:absolute;left:512px;top:592px;width:88px;height:88px;border-radius:50%;background:var(--seal);box-shadow:inset 0 0 0 8px #8a0e15}
  .producer-line{position:absolute;left:0;width:650px;top:700px;text-align:center;font-family:'Cinzel',serif;font-weight:600;font-size:12px;letter-spacing:1.5px;color:var(--gold)}
</style>
</head>
<body>
<main class="canvas">

  <section class="neck-label" aria-label="Neck label">
    <div class="neck-label__band"></div>
    <svg class="neck-label__edge" width="112" height="8" viewBox="0 0 112 8">
      <defs>
        <pattern id="neck-zigzag" width="8" height="8" patternUnits="userSpaceOnUse">
          <path d="M0 0 L4 8 L8 0 Z" fill="#14110e"/>
        </pattern>
      </defs>
      <rect width="112" height="8" fill="url(#neck-zigzag)"/>
    </svg>
    <div class="neck-label__title">Gran Reserva</div>
    <div class="neck-label__sub">Very Special<br>Pot Still</div>
    <div class="neck-label__script">Brandy</div>
  </section>

  <section class="front-label" aria-label="Front label">
    <div class="front-label__mountains" role="img" aria-label="Engraved alpine mountain range illustration in deep blue tones"></div>
    <div class="front-label__base"></div>

    <div class="swiss-flag" role="img" aria-label="Swiss flag"></div>
    <div class="brand-name">Velorin</div>
    <div class="brand-tagline">SWISS DISTILLERY</div>

    <h1 class="product-title">Gran Reserva</h1>
    <div class="product-subtitle">Very Special Pot Still</div>
    <div class="product-type">Brandy</div>

    <div class="info-panel">
      <svg width="496" height="180" viewBox="0 0 496 180">
        <defs>
          <pattern id="panel-top" width="8" height="8" patternUnits="userSpaceOnUse">
            <path d="M0 8 L4 0 L8 8 Z" fill="#f2ede2"/>
          </pattern>
          <pattern id="panel-bottom" width="8" height="8" patternUnits="userSpaceOnUse">
            <path d="M0 0 L4 8 L8 0 Z" fill="#f2ede2"/>
          </pattern>
        </defs>
        <rect x="0" y="0" width="496" height="8" fill="url(#panel-top)"/>
        <rect x="0" y="8" width="496" height="164" fill="#f2ede2"/>
        <rect x="0" y="172" width="496" height="8" fill="url(#panel-bottom)"/>
      </svg>
      <p class="info-panel__story">This brandy is crafted from carefully selected grapes, distilled in Copper Pot Stills, and aged for at least 6 years in French Oak Barrels. The long aging process allows the Brandy to develop complex flavors and a smooth, rich character.</p>
      <div class="info-panel__age">
        <div class="info-panel__age-label">Aged</div>
        <div class="info-panel__age-number">6</div>
        <div class="info-panel__age-unit">Years</div>
      </div>
      <ul class="tasting-notes">
        <li><b>Colour:</b> rich golden colour</li>
        <li><b>Aroma:</b> ripe apple with hints of vanilla</li>
        <li><b>Taste:</b> spicy with fruity palate</li>
        <li><b>Finish:</b> well balanced with a fruity aftertaste</li>
      </ul>
      <div class="info-panel__barrels">
        <span>Aged in French</span>
        <span class="barrel-icon" role="img" aria-label="Oak barrels illustration"></span>
        <span>Oak Barrels</span>
      </div>
      <div class="info-panel__abv">45% Alc. Vol. &nbsp;|&nbsp; 750 ml</div>
    </div>

    <div class="craft-seal" role="img" aria-label="Red wax seal, hand-crafted small batch"></div>
    <div class="producer-line">Produced by Velorin Swiss Distillery, Switzerland</div>
  </section>

</main>
</body>
</html>
```